Book & e-book cover - front, back and sleeve

Please see plot description:

The Lantern

A man lies dying and trapped in a parking garage stairwell. The poorly lit stairwell serves as a painful reminder of one of his memories of childhood locked in that darkened closet. To keep himself in tact he would play with a shiny silver button he ripped off from his pajamas – throwing it in the air and tapping the floor to find it. As he lies trapped and dying that same defeated and abandoned feeling descends upon him. As he comes in and out of consciousness memories from his past manifest themselves and we are introduced to the turbulent and sometimes triumphant pathway that has led him to his current state. It is up to him to sort through the barrage of emotions to find his way out, to let go, to forgive. That is if his heart will let him.
Updates

I know that we mentioned having a photograph of a button on the cover but we would like to see examples of covers with a more abstract or drawn or painted looking button.  Thanks.

Target Market(s)

Dramatic story - geared towards adult readers

Industry/Entity Type

Parking

Requirements
Must have
• Simple, crisp, custom, classic look. Do not want it to look to sci-fi or medival - this is an emotional story - a memoir.

Items on the front cover:

Title: The Lantern
Author: R.M. Halvorsen
Words: A Novel
Photo: a sliver button (just one image)

Items on the back cover

Plot description area
ISBN area at bottom

Nice to have
• Please see examples that have been uploaded. I like novels with a textured background.

A simple button on the cover with the right fonts and colour scheme.
Should not have
• I do not want a person or icons used on the cover
I do not want it to busy.
Do not want it to feel like it is a sci-fi novel or medival story.
Do not want the cover to be too "dark" - I do not want potential readers to get the wrong idea of what "The Lantern" is about.

```html
<!DOCTYPE html>
<html lang="en">
<head>
<meta charset="utf-8">
<title>The Lantern – cover, front and back</title>
<link href="https://fonts.googleapis.com/css2?family=Roboto:wght@100;300;400&display=swap" rel="stylesheet">
<style>
  :root {
    --backdrop: #f1f2f3;
    --cover-deep: #4f86b8;
    --cover-mid: #7aa7c9;
    --cover-light: #b3d1da;
    --ink-white: #ffffff;
    --ink-soft: #eef5f8;
    --button-light: #e7e5dc;
    --button-mid: #b9b6aa;
    --button-dark: #8d8a80;
  }
  * { margin: 0; padding: 0; box-sizing: border-box; }
  html, body {
    width: 1200px; height: 808px; overflow: hidden;
    background: var(--backdrop);
  }
  .spread {
    position: relative; width: 1200px; height: 808px;
    font-family: "Roboto", Arial, sans-serif;
  }
  .cover {
    position: absolute; top: 34px; width: 418px; height: 628px;
    overflow: hidden;
    background:
      radial-gradient(ellipse 55% 40% at 60% 60%, var(--cover-light) 0%, transparent 100%),
      radial-gradient(ellipse 60% 45% at 45% 35%, rgba(179,209,218,0.7) 0%, transparent 100%),
      linear-gradient(160deg, var(--cover-deep) 0%, var(--cover-mid) 45%, var(--cover-mid) 70%, var(--cover-deep) 100%);
    box-shadow: 0 6px 14px rgba(0,0,0,0.18);
  }
  .cover--front { left: 36px; }
  .cover--back { left: 488px; }

  /* Front */
  .title-small {
    position: absolute; left: 256px; top: 122px;
    font-weight: 300; font-size: 40px; color: var(--ink-white);
  }
  .title-main {
    position: absolute; left: 36px; top: 168px;
    font-weight: 100; font-size: 104px; letter-spacing: -2px;
    color: var(--ink-white); line-height: 1;
  }
  .button-art {
    position: absolute; border-radius: 50%;
    background: radial-gradient(circle at 38% 35%, var(--button-light) 0%, var(--button-mid) 60%, var(--button-dark) 100%);
    box-shadow: 0 2px 6px rgba(0,0,0,0.3);
  }
  .button-art--front { left: 344px; top: 140px; width: 56px; height: 56px; }
  .tagline {
    position: absolute; left: 190px; top: 346px;
    font-weight: 300; font-size: 17px; letter-spacing: 3px;
    color: var(--ink-white);
  }
  .author {
    position: absolute; left: 0; width: 100%; top: 546px;
    text-align: center; font-weight: 300; font-size: 34px;
    color: var(--ink-white);
  }

  /* Back */
  .blurb {
    position: absolute; left: 39px; top: 76px; width: 342px;
    font-size: 10.4px; line-height: 14.6px; color: var(--ink-soft);
    letter-spacing: 0.15px;
  }
  .blurb p { text-align: justify; margin-bottom: 14px; }
  .blurb .closing { display: block; text-align: center; }
  .button-art--back { left: -40px; top: 492px; width: 180px; height: 180px; }
  .isbn-box {
    position: absolute; left: 260px; top: 528px;
    width: 78px; height: 86px;
    border: 1px solid rgba(255,255,255,0.8);
  }
</style>
</head>
<body>
<div class="spread">
  <section class="cover cover--front">
    <div class="title-small">the</div>
    <h1 class="title-main">lantern</h1>
    <div class="button-art button-art--front" role="img" aria-label="Painted silver button with four holes, sewn with dark thread"></div>
    <div class="tagline">a novel</div>
    <div class="author">R.M. Halvorsen</div>
  </section>

  <section class="cover cover--back">
    <div class="blurb">
      <p>Evan Marlowe is half-dead. Maybe fully dead. He feels that way most days. What keep him barely alive are pills, bitter hatred and a button. The button is bright and shiny in a way that his childhood was not. It is the object of comfort he clings to obsessively, reliving fragments of his past with every stroke of his fingertip. But in the same way that the button won't let him forget, his misery reflected back at him in the form of his wife, his child, his employees is forcing him to remember.
      <span class="closing">That - and the chest pains.</span></p>
      <p>Collapsed in the stairwell of his law firm he is unable to move and unable to escape. He comes in and out of consciousness, defenseless against repressed memories of a cold home and a merciless mother now painfully playing in his psyche. We are introduced to the turbulent and sometimes triumphant pathways that have led to his current state. Evan must face the brutality of his upbringing to find his way out, to let go, to forgive.
      <span class="closing">That is, if his heart will let him.</span></p>
      <p>The Lantern is an intense and empowering depiction of how the imprint of childhood stays with us forever, and how it
      <span class="closing">leaves a blueprint for a better being.</span></p>
    </div>
    <div class="button-art button-art--back" role="img" aria-label="Close-up of the silver button with thread trailing away"></div>
    <div class="isbn-box"></div>
  </section>
</div>
</body>
</html>
```